Business cards for a new business: Amber Willow Dawn Healing

I would like for the card to include a lotus. The business is a healing practice so I'd like the overall colours to be pink and green and for it to have a soft feel. The name of the practice is
"Amber Willow Dawn Healing", which I'd like to be included, as well as the words: "Energetic and spiritual healing to restore health, harmony and wellbeing". Also, my name - Tovan and the number: 5319 6048

Target Market(s)

Everyone interested in personal healing!

Industry/Entity Type

Business

Contact Information for Business Card

As above……..could be single or double-sided
I'd like the font for the name of the practice and my name to be in green and be a flowing, but simple font - elegant.
The background to be a light pink. See below for colours

Colors
f9d9e8
eea4c8
e567a6
d0ebe7
86cfc6
33b7a4

Requirements
Must have
• See above
Nice to have
• See above

```html
<!DOCTYPE html>
<html lang="en">
<head>
<meta charset="utf-8">
<title>Amber Willow Dawn Healing – Business Card</title>
<link rel="stylesheet" href="https://fonts.googleapis.com/css2?family=Questrial&family=Lora:wght@700&display=swap">
<style>
  :root {
    --page-bg: #ece7e9;
    --card-pink: #fbe9f1;
    --blush: #f9d9e8;
    --rose: #eea4c8;
    --mint: #d0ebe7;
    --aqua: #86cfc6;
    --teal: #33b7a4;
    --teal-deep: #26998a;
    --white: #ffffff;
  }
  html, body {
    margin: 0;
    width: 1200px;
    height: 1023px;
    overflow: hidden;
    background: var(--page-bg);
  }
  .card {
    position: absolute;
    left: 150px;
    top: 254px;
    width: 900px;
    height: 514px;
    border-radius: 28px;
    overflow: hidden;
    box-shadow: 0 10px 30px rgba(0,0,0,0.15);
  }
  .card svg { display: block; }
  .brand-name {
    font-family: "Questrial", sans-serif;
    font-size: 30px;
    fill: var(--teal-deep);
  }
  .tagline {
    font-family: "Questrial", sans-serif;
    font-size: 16.5px;
    fill: var(--teal-deep);
    letter-spacing: 0.3px;
  }
  .holder-name {
    font-family: "Lora", serif;
    font-weight: 700;
    font-size: 40px;
    fill: var(--white);
  }
  .contact {
    font-family: "Questrial", sans-serif;
    font-size: 20px;
    fill: var(--white);
  }
  .contact-email {
    font-size: 19px;
  }
</style>
</head>
<body>
  <div class="card">
    <svg width="900" height="514" viewBox="0 0 900 514" xmlns="http://www.w3.org/2000/svg">
      <defs>
        <linearGradient id="card-face" x1="0" y1="0" x2="1" y2="1">
          <stop offset="0" stop-color="var(--card-pink)"/>
          <stop offset="1" stop-color="var(--blush)"/>
        </linearGradient>
        <linearGradient id="wave-fill" x1="0" y1="0" x2="1" y2="1">
          <stop offset="0" stop-color="var(--aqua)"/>
          <stop offset="0.45" stop-color="var(--teal)"/>
          <stop offset="1" stop-color="var(--teal-deep)"/>
        </linearGradient>
        <path id="tagline-curve" d="M268,500 C500,400 560,170 640,6"/>
      </defs>

      <rect class="card-face" width="900" height="514" fill="url(#card-face)"/>

      <path class="wave-outer" d="M668,0 C585,170 530,400 250,514 L900,514 L900,0 Z" fill="url(#wave-fill)"/>
      <path class="wave-stripe" d="M705,0 C630,180 580,410 330,514 L355,514 C610,410 660,180 728,0 Z" fill="var(--white)" opacity="0.9"/>

      <text class="tagline">
        <textPath href="#tagline-curve">Energetic and spiritual healing to restore health, harmony and wellbeing</textPath>
      </text>

      <text class="brand-name" x="290" y="150" text-anchor="middle">Amber Willow Dawn Healing</text>
      <circle class="brand-mark" cx="290" cy="270" r="78" fill="var(--rose)"/>

      <text class="holder-name" x="870" y="118" text-anchor="end">Tovan</text>
      <text class="contact" x="870" y="158" text-anchor="end">5319 6048</text>
      <text class="contact contact-email" x="870" y="196" text-anchor="end">tovan@willowmail.com</text>
    </svg>
  </div>
</body>
</html>
```